Digital Billboard to Drive Buying Local

We are a Montana-based soap and hygiene product company (think Dr. Bramblor and Hollet). We are looking to design a billboard ad for some digital billboards around Montana. We will have 8 seconds at a time to make an impression so we need a quick and to the point ad. We are thinking a line like "Bring Montana inside. Far Drift, Natural Soap." (Far Drift is the name of one of our soaps and is also the unofficial slogan for Montana.) Our products are made in Montana and we want to appeal to both people that appreciate that as well as outdoors lovers. I'll attach a picture of the soap box, our logo, website and a couple of examples of billboards from companies like Baron Tolvey and Sundrick Pell. Let me know if you need higher-resolution images.
Website: BrisklynLatherCo.com
Company Name: Brisklyn Lather Co.

```html
<!DOCTYPE html>
<html lang="en">
<head>
<meta charset="utf-8">
<title>Brisklyn Lather Co. — Billboard</title>
<link href="https://fonts.googleapis.com/css2?family=Bebas+Neue&family=League+Spartan:wght@700;800&family=Montserrat:wght@500;700&family=Oswald:wght@400;500&display=swap" rel="stylesheet">
<style>
  :root {
    --page-bg: #3f302e;
    --sky-slate: #5d6f80;
    --mountain-blue: #3b5566;
    --mist: #7f97a3;
    --wood-light: #8a6547;
    --wood-dark: #3e2a1d;
    --headline-white: #ffffff;
    --brand-green: #8fd86a;
    --pill-brown: #4a2f22;
    --pill-text: #b9dc9c;
    --kraft: #c99c52;
    --kraft-dark: #a97e3d;
    --ink: #3a2a1c;
    --box-teal: #6f9a9a;
    --box-teal-deep: #3f6f75;
    --soap-green: #7fae8c;
    --box-gold: #e0a93a;
  }
  * { margin: 0; padding: 0; box-sizing: border-box; }
  html, body { width: 889px; height: 1200px; overflow: hidden; }
  body { background: var(--page-bg); position: relative; }

  .billboard {
    position: absolute;
    left: 44px; top: 400px;
    width: 800px; height: 400px;
    overflow: hidden;
    box-shadow: 0 8px 24px rgba(0,0,0,.45);
  }
  .scenery {
    position: absolute; inset: 0;
    background: linear-gradient(180deg,
      var(--mist) 0%, var(--sky-slate) 14%, var(--mountain-blue) 38%,
      #4a5a5c 56%, var(--wood-light) 66%, #6b4b33 82%, var(--wood-dark) 100%);
  }

  .brand {
    position: absolute;
    left: 37px; top: 40px;
    width: 120px;
    display: flex; flex-direction: column; align-items: center; gap: 8px;
  }
  .brand .mark { width: 40px; height: 40px; background: var(--headline-white); }
  .brand .name {
    font-family: "Bebas Neue", sans-serif;
    font-size: 16px; letter-spacing: 1.4px; line-height: 1;
    color: var(--headline-white); white-space: nowrap;
  }

  .tagline {
    position: absolute;
    left: 173px; top: 34px;
    font-family: "Bebas Neue", sans-serif;
    font-weight: 400;
    font-size: 68px; line-height: 1;
    letter-spacing: 4.4px;
    color: var(--headline-white);
    white-space: nowrap;
    text-shadow: 0 2px 8px rgba(0,0,0,.4);
  }
  .product-name {
    position: absolute;
    left: 35px; top: 136px;
    font-family: "League Spartan", sans-serif;
    font-weight: 800; font-size: 92px; line-height: 1;
    color: var(--brand-green); white-space: nowrap;
    text-shadow: 0 3px 10px rgba(0,0,0,.35);
  }
  .product-type {
    position: absolute;
    left: 37px; top: 206px;
    font-family: "League Spartan", sans-serif;
    font-weight: 800; font-size: 58px; line-height: 1;
    color: var(--headline-white); white-space: nowrap;
    text-shadow: 0 3px 10px rgba(0,0,0,.35);
  }
  .site-pill {
    position: absolute;
    left: 37px; top: 277px;
    width: 386px; height: 40px;
    border-radius: 20px;
    background: var(--pill-brown);
    display: flex; align-items: center; justify-content: center;
    font-family: "Montserrat", sans-serif;
    font-weight: 700; font-size: 21px; letter-spacing: 2.6px;
    color: var(--pill-text);
  }

  /* soap box */
  .box-side, .box-front {
    position: absolute; top: 102px; height: 217px;
    background: var(--kraft);
    box-shadow: 0 6px 16px rgba(0,0,0,.45);
  }
  .box-side {
    left: 486px; width: 80px;
    background: linear-gradient(90deg, var(--kraft-dark), var(--kraft) 40%);
    display: flex; flex-direction: column; align-items: center;
    padding-top: 10px; gap: 8px;
    font-family: "Montserrat", sans-serif; font-weight: 500;
    font-size: 7.5px; line-height: 1.15; color: var(--ink); text-align: center;
  }
  .claim { display: flex; align-items: center; gap: 3px; }
  .claim .dot {
    flex: none; width: 12px; height: 12px; border-radius: 50%;
    border: 1.2px solid var(--ink);
  }
  .origin { margin-top: 4px; }
  .flag { width: 34px; height: 20px; background: #5a4a3a; margin-top: 4px; }

  .box-front { left: 571px; width: 159px; overflow: hidden; }
  .front-art {
    position: absolute; inset: 0;
    background: linear-gradient(180deg, var(--kraft) 0%, var(--kraft) 44%,
      #b8c6b8 50%, var(--box-teal) 62%, var(--box-teal-deep) 100%);
  }
  .soap-window {
    position: absolute; left: 117px; top: 11px;
    width: 31px; height: 99px; border-radius: 14px;
    background: var(--soap-green);
  }
  .front-brand {
    position: absolute; left: 10px; top: 50px;
    font-family: "Oswald", sans-serif; font-size: 9px;
    letter-spacing: 1px; color: #fff;
  }
  .front-title {
    position: absolute; left: 8px; top: 138px;
    font-family: "Oswald", sans-serif; font-weight: 500;
    font-size: 22px; line-height: 1; color: var(--box-gold);
  }
  .front-sub {
    position: absolute; left: 8px; top: 162px;
    font-family: "Oswald", sans-serif; font-size: 10px; color: #1e2a2a;
  }
  .front-detail {
    position: absolute; left: 8px; top: 178px;
    font-family: "Oswald", sans-serif; font-size: 8px; line-height: 1.1;
    color: #d9c98a;
  }
  .front-foot {
    position: absolute; left: 8px; right: 6px; top: 202px;
    display: flex; justify-content: space-between;
    font-family: "Oswald", sans-serif; font-size: 7.5px; color: #e7eef0;
  }
</style>
</head>
<body>
  <section class="billboard">
    <div class="scenery" role="img" aria-label="Misty Montana mountain range above a weathered wooden tabletop"></div>

    <div class="brand">
      <span class="mark"></span>
      <span class="name">Brisklyn Lather Co.</span>
    </div>

    <h1 class="tagline">BRING MONTANA INSIDE.</h1>
    <p class="product-name">FAR DRIFT</p>
    <p class="product-type">NATURAL SOAP</p>
    <p class="site-pill">BrisklynLatherCo.com</p>

    <div class="box-side">
      <div class="claim"><span class="dot"></span><span>100%<br>Recyclable</span></div>
      <div class="claim"><span class="dot"></span><span>Paraben<br>Free</span></div>
      <div class="claim"><span class="dot"></span><span>Phthalate<br>Free</span></div>
      <div class="claim"><span class="dot"></span><span>Natural<br>Sustainable<br>Ingredients</span></div>
      <div class="origin">Born In<br>Montana<br>Raised<br>Nomadic.</div>
      <div class="flag"></div>
    </div>

    <div class="box-front">
      <div class="front-art" role="img" aria-label="Topographic contour pattern above a teal mountain and pine tree scene"></div>
      <div class="soap-window" role="img" aria-label="Green soap bar seen through the box window"></div>
      <p class="front-brand">BRISKLYN LATHER CO.</p>
      <p class="front-title">Far Drift</p>
      <p class="front-sub">(In Nature)</p>
      <p class="front-detail">All Natural<br>Bar Soap</p>
      <p class="front-foot"><span>Mmm...Smells Like Mountains</span><span>5.25oz</span></p>
    </div>
  </section>
</body>
</html>
```